Halvern Ridge Plants and Nursery needs a business street sign.

I have three businesses located at the same address: The Halvern Ridge Plants & Nursery, The Marrow Stall, and The Brackett Commons. I am looking for a 4’ x 8’ street sign to represent all three businesses as one retail experience. It needs to be eye catching yet simple enough that people can fully read it while driving by. I have logos for the greenhouse and village however I do not have anything for The Marrow Stall. I’m looking for some type of font that’s similar or in between the two attached logos for The Marrow Stall.

Requirements
Must have
• Horizontal Sign, Eye catching, yet simple design so people see it while driving by.
Nice to have
• Horizontal Sign
Should not have
• I’m open to the design being both vertical and horizontal. Please provide both options

```html
<!DOCTYPE html>
<html lang="en">
<head>
<meta charset="utf-8">
<title>Halvern Ridge Plants &amp; Nursery – Street Sign</title>
<link rel="stylesheet" href="https://fonts.googleapis.com/css2?family=Catamaran:wght@700&display=swap">
<style>
  :root {
    --backdrop: #eef0ee;
    --frame-green: #234d35;
    --frame-white: #ffffff;
    --panel-brown: #3a1b1d;
    --letter-cream: #eeecd8;
    --bloom-white: #f4f3ea;
    --bloom-leaf: #2f7a55;
    --bloom-yellow: #f1c526;
  }
  html, body {
    margin: 0;
    padding: 0;
    width: 1200px;
    height: 986px;
    overflow: hidden;
    background: var(--backdrop);
  }
  .sign {
    position: relative;
    width: 1200px;
    height: 986px;
    font-family: "Catamaran", sans-serif;
    font-weight: 700;
    color: var(--letter-cream);
  }
  .sign-board {
    position: absolute;
    left: 20px;
    top: 158px;
    width: 1160px;
    height: 670px;
  }
  .board-panel { fill: var(--panel-brown); stroke: var(--frame-green); stroke-width: 48; }
  .board-band { fill: none; stroke: var(--frame-white); stroke-width: 20; }
  .bloom-cluster {
    position: absolute;
    left: 545px;
    top: 214px;
    width: 110px;
    height: 46px;
    border-radius: 23px;
    background: radial-gradient(ellipse at center, var(--bloom-white) 0%, var(--bloom-yellow) 40%, var(--bloom-leaf) 78%, rgba(47,122,85,0) 100%);
  }
  .brand {
    position: absolute;
    left: 0;
    width: 1200px;
    text-align: center;
    margin: 0;
    line-height: 1;
  }
  .brand-main {
    top: 336px;
    font-size: 76px;
  }
  .brand-sub {
    top: 440px;
    font-size: 30px;
    letter-spacing: 2px;
    text-transform: uppercase;
  }
  .tenant {
    position: absolute;
    top: 590px;
    width: 420px;
    margin: 0;
    text-align: center;
    font-size: 60px;
    line-height: 1.05;
  }
  .tenant-commons { left: 250px; }
  .tenant-stall { left: 675px; }
  .tenant span { display: block; }
</style>
</head>
<body>
<main class="sign">
  <svg class="sign-board" viewBox="-30 -30 1160 670" aria-hidden="true">
    <defs>
      <path id="board-shape" d="M40,110 H330 C360,110 380,0 550,0 C720,0 740,110 770,110 H1060 A40,40 0 0 0 1100,150 V570 A40,40 0 0 0 1060,610 H40 A40,40 0 0 0 0,570 V150 A40,40 0 0 0 40,110 Z"/>
    </defs>
    <use href="#board-shape" class="board-panel"/>
    <use href="#board-shape" class="board-band"/>
  </svg>

  <div class="bloom-cluster" role="img" aria-label="Small cluster of white daisies and yellow blossoms with green leaves"></div>

  <h1 class="brand brand-main">The Halvern Ridge</h1>
  <p class="brand brand-sub">Plants &amp; Nursery</p>

  <p class="tenant tenant-commons"><span>Brackett</span><span>Commons</span></p>
  <p class="tenant tenant-stall"><span>The Marrow</span><span>Stall</span></p>
</main>
</body>
</html>
```